Mandarin tuition, language and travel services

We need a website for a new startup company, which offers Mandarin tuition, translating and interpreting, and travel services. Our company is based in Jersey, a British channel island. We would like a creative and modern professional website. Preferably with some animations. The attached is a website, which style we would prefer:
http://www.quorvabelt.net/
We have also attached our logo for your reference
We would also like to see designs using black, red and orange, which corresponds with our logo colours. The cartoon images could be travel resorts in China, and the president of China waving to the web-browsers. Of course, we wouldn't wish to restrain the designers creativity. Any creative and interesting ideas are welcomed! We look forward to hearing from you!

Target Market(s)

school children and adults

Industry/Entity Type

It Company

Number of Pages Required

3 page

Requirements
Must have
• We would prefer a small 3 pages website, if possible. The 3 pages need to be Services, News Room, and Contact us.

```html
<!DOCTYPE html>
<html lang="en">
<head>
<meta charset="utf-8">
<title>Lotus Lingua</title>
<link rel="stylesheet" href="https://fonts.googleapis.com/css2?family=Alfa+Slab+One&family=Open+Sans:wght@400;600;700&display=swap">
<style>
:root{
  --ink:#1b1b1b;
  --ink-soft:#232323;
  --red:#d7161c;
  --gold:#e8b21c;
  --card:#fdd023;
  --white:#ffffff;
  --text-soft:#e4e4e4;
  --line:#5a5a5a;
}
*{margin:0;padding:0;box-sizing:border-box}
html,body{width:1200px;height:2247px;overflow:hidden}
body{background:var(--ink);font-family:"Open Sans",Arial,sans-serif;color:var(--white);position:relative}

.site-header{position:absolute;top:0;left:0;width:1200px;height:181px;background:var(--ink)}
.round-btn{position:absolute;top:43px;width:52px;height:52px;border-radius:50%;background:var(--red);display:flex;align-items:center;justify-content:center}
.round-btn.phone{left:74px}
.round-btn.mail{right:74px}
.brand{position:absolute;top:40px;left:0;width:1200px;text-align:center;font-family:"Open Sans",Arial,sans-serif;font-weight:700;font-size:30px;color:var(--white)}
.brand-dot{display:inline-block;width:22px;height:22px;border-radius:50%;background:var(--red);vertical-align:middle;margin-left:8px}
.main-nav{position:absolute;top:134px;left:0;width:1200px;display:flex;justify-content:center;align-items:center;gap:18px}
.main-nav a{color:var(--white);text-decoration:none;font-weight:700;font-size:19px;letter-spacing:.2px}
.nav-sep{width:8px;height:20px;background:var(--gold);border-radius:3px}

.hero{position:absolute;top:181px;left:0;width:1200px;height:590px;background:linear-gradient(180deg,#eef0e6 0%,#d9c996 28%,#9c8d2a 48%,#c09a3a 62%,#7a7a24 82%,#5f6a2a 100%)}
.hero-arrow{position:absolute;top:456px;width:36px;height:36px;border-radius:50%;background:#1a1a1a;border:2px solid var(--white);display:flex;align-items:center;justify-content:center}
.hero-arrow.prev{left:43px}
.hero-arrow.next{right:43px}

.welcome{position:absolute;top:821px;left:75px;width:1052px;height:449px}
.frame-line{position:absolute;background:var(--line)}
.corner{position:absolute;width:38px;height:38px;background:var(--gold)}
.section-title{font-family:"Alfa Slab One",Georgia,serif;font-size:36px;text-align:center;color:var(--white);letter-spacing:.5px;font-weight:400}
.section-title em{font-style:normal;color:var(--red)}
.title-rule{position:relative;width:520px;height:2px;background:#3d3d3d;margin:0 auto}
.title-mark{position:absolute;left:50%;top:-8px;width:74px;height:16px;margin-left:-37px;background:var(--gold);border-radius:8px}
.welcome .section-title{position:absolute;top:70px;left:0;width:100%}
.welcome .title-rule{position:absolute;top:136px;left:266px}
.welcome-copy{position:absolute;top:178px;left:64px;width:928px;text-align:center;font-size:14.6px;line-height:24px;color:var(--text-soft)}

.offers-title{position:absolute;top:1325px;left:0;width:1200px}
.offers-rule{position:absolute;top:1393px;left:340px}

.cards{position:absolute;top:1438px;left:75px;width:1052px;height:578px}
.card{position:absolute;top:0;width:332px;height:578px;background:var(--card);color:var(--ink)}
.card:nth-child(1){left:0}
.card:nth-child(2){left:360px}
.card:nth-child(3){left:720px}
.card .c-line{position:absolute;background:var(--ink)}
.card .c-corner{position:absolute;width:30px;height:30px;background:var(--ink)}
.card-photo{position:absolute;top:54px;left:57px;width:218px;height:218px;border-radius:50%;border:4px solid var(--ink)}
.card h3{position:absolute;top:286px;left:0;width:100%;text-align:center;font-size:22.5px;line-height:25px;font-weight:700}
.card-rule{position:absolute;top:352px;left:74px;width:184px;height:2px;background:var(--ink)}
.card p{position:absolute;top:378px;left:30px;width:272px;text-align:center;font-size:15px;line-height:24px}
.read-more{position:absolute;top:528px;left:100px;width:132px;height:34px;border-radius:17px;background:var(--ink);color:var(--card);font-weight:700;font-size:14.5px;display:flex;align-items:center;justify-content:center;gap:10px;text-decoration:none}
.read-more span.ico{width:22px;height:22px;border-radius:50%;border:2px solid var(--card);display:flex;align-items:center;justify-content:center}

.site-footer{position:absolute;top:2090px;left:0;width:1200px;height:157px;background:var(--red)}
.contact-item{position:absolute;top:25px;display:flex;gap:14px;font-size:14px;line-height:21px;color:var(--white)}
.contact-item .ico{width:28px;height:28px;border-radius:50%;border:2px solid var(--white);display:flex;align-items:center;justify-content:center;flex:none}
.social{position:absolute;top:26px;right:72px;display:flex;gap:6px}
.social span{width:31px;height:31px;border-radius:50%;border:2px solid var(--white)}
.foot-nav{position:absolute;top:122px;left:73px;display:flex;gap:18px}
.foot-nav a{color:var(--white);text-decoration:none;font-size:15px}
.copyright{position:absolute;top:122px;right:70px;font-size:15px;color:var(--white)}
</style>
</head>
<body>

<header class="site-header">
  <a class="round-btn phone" aria-label="Call us">
    <svg width="24" height="24" viewBox="0 0 24 24"><path d="M6.6 10.8c1.4 2.8 3.8 5.1 6.6 6.6l2.2-2.2c.3-.3.7-.4 1-.2 1.1.4 2.3.6 3.6.6.6 0 1 .4 1 1V20c0 .6-.4 1-1 1C10.6 21 3 13.4 3 4c0-.6.4-1 1-1h3.5c.6 0 1 .4 1 1 0 1.3.2 2.5.6 3.6.1.3 0 .7-.2 1L6.6 10.8z" fill="none" stroke="#fff" stroke-width="1.6"/></svg>
  </a>
  <div class="brand">Lotus Lingua<span class="brand-dot"></span></div>
  <a class="round-btn mail" aria-label="Email us">
    <svg width="26" height="20" viewBox="0 0 26 20"><rect x="1" y="1" width="24" height="18" fill="none" stroke="#fff" stroke-width="1.8"/><path d="M1 1l12 10L25 1M1 19l9-8M25 19l-9-8" fill="none" stroke="#fff" stroke-width="1.6"/></svg>
  </a>
  <nav class="main-nav">
    <a href="#">HOME</a><span class="nav-sep"></span>
    <a href="#">ABOUT US</a><span class="nav-sep"></span>
    <a href="#">SERVICES</a><span class="nav-sep"></span>
    <a href="#">NEWS ROOM</a><span class="nav-sep"></span>
    <a href="#">CONTACT US</a>
  </nav>
</header>

<section class="hero" role="img" aria-label="Chinese pavilion among autumn trees reflected in a calm lake">
  <span class="hero-arrow prev"><svg width="14" height="14" viewBox="0 0 14 14"><path d="M9 2L4 7l5 5" fill="none" stroke="#fff" stroke-width="2"/></svg></span>
  <span class="hero-arrow next"><svg width="14" height="14" viewBox="0 0 14 14"><path d="M5 2l5 5-5 5" fill="none" stroke="#fff" stroke-width="2"/></svg></span>
</section>

<section class="welcome">
  <span class="frame-line" style="top:18px;left:40px;width:972px;height:1px"></span>
  <span class="frame-line" style="top:26px;left:40px;width:972px;height:1px"></span>
  <span class="frame-line" style="bottom:18px;left:40px;width:972px;height:1px"></span>
  <span class="frame-line" style="bottom:26px;left:40px;width:972px;height:1px"></span>
  <span class="frame-line" style="top:40px;left:10px;width:1px;height:369px"></span>
  <span class="frame-line" style="top:40px;left:18px;width:1px;height:369px"></span>
  <span class="frame-line" style="top:40px;right:10px;width:1px;height:369px"></span>
  <span class="frame-line" style="top:40px;right:18px;width:1px;height:369px"></span>
  <span class="corner" role="img" aria-label="Gold scroll ornament" style="top:0;left:0"></span>
  <span class="corner" role="img" aria-label="Gold scroll ornament" style="top:0;right:0"></span>
  <span class="corner" role="img" aria-label="Gold scroll ornament" style="bottom:0;left:0"></span>
  <span class="corner" role="img" aria-label="Gold scroll ornament" style="bottom:0;right:0"></span>
  <h2 class="section-title">WELCOME TO <em>LOTUS LINGUA</em></h2>
  <div class="title-rule"><span class="title-mark" role="img" aria-label="Gold scroll ornament"></span></div>
  <p class="welcome-copy">Lorem ipsum dolor sit amet, consectetur adipiscing elit, sed do eiusmod tempor incididunt ut labore et dolore magna aliqua. Ut enim ad minim veniam, quis nostrud exercitation ullamco laboris nisi ut aliquip ex ea commodo consequat. Duis aute irure dolor in reprehenderit in voluptate velit esse cillum dolore eu fugiat nulla pariatur. Excepteur sint occaecat cupidatat non proident, sunt in culpa qui officia deserunt mollit anim id est laborum. Sed ut perspiciatis unde omnis iste natus error sit voluptatem accusantium doloremque laudantium, totam rem aperiam, eaque ipsa quae ab illo inventore veritatis et quasi architecto beatae vitae dicta sunt explicabo. Nemo enim ipsam voluptatem quia voluptas sit aspernatur aut odit aut fugit, sed quia consequuntur magni dolores eos qui ratione voluptatem sequi nesciunt. Neque porro quisquam est, qui dolorem ipsum quia dolor sit amet, consectetur, adipisci velit, sed quia non numquam eius modi tempora incidunt ut labore et dolore magnam aliquam quaerat voluptatem.</p>
</section>

<h2 class="section-title offers-title">WHAT WE <em>OFFERS</em></h2>
<div class="title-rule offers-rule"><span class="title-mark" role="img" aria-label="Gold scroll ornament"></span></div>

<section class="cards">
  <article class="card">
    <span class="c-line" style="top:30px;left:54px;width:224px;height:2px"></span>
    <span class="c-line" style="bottom:30px;left:54px;width:224px;height:2px"></span>
    <span class="c-line" style="top:54px;left:18px;width:2px;height:470px"></span>
    <span class="c-line" style="top:54px;right:18px;width:2px;height:470px"></span>
    <span class="c-corner" role="img" aria-label="Scroll ornament" style="top:10px;left:10px"></span>
    <span class="c-corner" role="img" aria-label="Scroll ornament" style="top:10px;right:10px"></span>
    <span class="c-corner" role="img" aria-label="Scroll ornament" style="bottom:10px;left:10px"></span>
    <span class="c-corner" role="img" aria-label="Scroll ornament" style="bottom:10px;right:10px"></span>
    <div class="card-photo" role="img" aria-label="Student writing Chinese characters on a glass board" style="background:linear-gradient(135deg,#c9d6e2,#8fa3b6 55%,#5b4636)"></div>
    <h3>Mandarin Tuition<br>Service</h3>
    <span class="card-rule"></span>
    <p>Lorem ipsum dolor sit amet, consectetur adipiscing elit, sed do eiusmod tempor incididunt ut labore et dolore magna aliqua. Ut enim ad minim.</p>
    <a class="read-more" href="#">Read More <span class="ico"><svg width="8" height="10" viewBox="0 0 8 10"><path d="M2 1l4 4-4 4" fill="none" stroke="#fdd023" stroke-width="1.8"/></svg></span></a>
  </article>
  <article class="card">
    <span class="c-line" style="top:30px;left:54px;width:224px;height:2px"></span>
    <span class="c-line" style="bottom:30px;left:54px;width:224px;height:2px"></span>
    <span class="c-line" style="top:54px;left:18px;width:2px;height:470px"></span>
    <span class="c-line" style="top:54px;right:18px;width:2px;height:470px"></span>
    <span class="c-corner" role="img" aria-label="Scroll ornament" style="top:10px;left:10px"></span>
    <span class="c-corner" role="img" aria-label="Scroll ornament" style="top:10px;right:10px"></span>
    <span class="c-corner" role="img" aria-label="Scroll ornament" style="bottom:10px;left:10px"></span>
    <span class="c-corner" role="img" aria-label="Scroll ornament" style="bottom:10px;right:10px"></span>
    <div class="card-photo" role="img" aria-label="Hands with pens over a document being translated" style="background:linear-gradient(135deg,#e6e8ea,#b9bec4 55%,#6f7379)"></div>
    <h3>Translating &amp;<br>Interpreting Service</h3>
    <span class="card-rule"></span>
    <p>Lorem ipsum dolor sit amet, consectetur adipiscing elit, sed do eiusmod tempor incididunt ut labore et dolore magna aliqua. Ut enim ad minim.</p>
    <a class="read-more" href="#">Read More <span class="ico"><svg width="8" height="10" viewBox="0 0 8 10"><path d="M2 1l4 4-4 4" fill="none" stroke="#fdd023" stroke-width="1.8"/></svg></span></a>
  </article>
  <article class="card">
    <span class="c-line" style="top:30px;left:54px;width:224px;height:2px"></span>
    <span class="c-line" style="bottom:30px;left:54px;width:224px;height:2px"></span>
    <span class="c-line" style="top:54px;left:18px;width:2px;height:470px"></span>
    <span class="c-line" style="top:54px;right:18px;width:2px;height:470px"></span>
    <span class="c-corner" role="img" aria-label="Scroll ornament" style="top:10px;left:10px"></span>
    <span class="c-corner" role="img" aria-label="Scroll ornament" style="top:10px;right:10px"></span>
    <span class="c-corner" role="img" aria-label="Scroll ornament" style="bottom:10px;left:10px"></span>
    <span class="c-corner" role="img" aria-label="Scroll ornament" style="bottom:10px;right:10px"></span>
    <div class="card-photo" role="img" aria-label="Great Wall of China winding over hills at sunset" style="background:linear-gradient(180deg,#e8d2a4,#b98a4e 50%,#5e4a2c)"></div>
    <h3>Travel<br>Service</h3>
    <span class="card-rule"></span>
    <p>Lorem ipsum dolor sit amet, consectetur adipiscing elit, sed do eiusmod tempor incididunt ut labore et dolore magna aliqua. Ut enim ad minim.</p>
    <a class="read-more" href="#">Read More <span class="ico"><svg width="8" height="10" viewBox="0 0 8 10"><path d="M2 1l4 4-4 4" fill="none" stroke="#fdd023" stroke-width="1.8"/></svg></span></a>
  </article>
</section>

<footer class="site-footer">
  <div class="contact-item" style="left:73px">
    <span class="ico"><svg width="12" height="14" viewBox="0 0 12 14"><path d="M6 13S1 7.8 1 5a5 5 0 0 1 10 0c0 2.8-5 8-5 8z" fill="none" stroke="#fff" stroke-width="1.5"/><circle cx="6" cy="5" r="1.7" fill="#fff"/></svg></span>
    <div>Your Company LTD.<br>Street Name, 000000<br>City Name</div>
  </div>
  <div class="contact-item" style="left:283px">
    <span class="ico"><svg width="13" height="13" viewBox="0 0 24 24"><path d="M6.6 10.8c1.4 2.8 3.8 5.1 6.6 6.6l2.2-2.2c.3-.3.7-.4 1-.2 1.1.4 2.3.6 3.6.6.6 0 1 .4 1 1V20c0 .6-.4 1-1 1C10.6 21 3 13.4 3 4c0-.6.4-1 1-1h3.5c.6 0 1 .4 1 1 0 1.3.2 2.5.6 3.6.1.3 0 .7-.2 1L6.6 10.8z" fill="#fff"/></svg></span>
    <div>Phone<br>1-000-000-0000</div>
  </div>
  <div class="contact-item" style="left:464px">
    <span class="ico"><svg width="13" height="10" viewBox="0 0 26 20"><rect x="1" y="1" width="24" height="18" fill="none" stroke="#fff" stroke-width="2.5"/><path d="M1 1l12 10L25 1" fill="none" stroke="#fff" stroke-width="2.5"/></svg></span>
    <div>Email<br>info@lotuslingua.com</div>
  </div>
  <div class="social" aria-label="Social links"><span></span><span></span><span></span><span></span></div>
  <nav class="foot-nav">
    <a href="#">HOME</a><a href="#">ABOUT US</a><a href="#">SERVICES</a><a href="#">NEWS ROOM</a><a href="#">CONTACT US</a>
  </nav>
  <div class="copyright">© 2016 LOTUS LINGUA. ALL RIGHTS RESERVED</div>
</footer>

</body>
</html>
```